Design Website appearance

Seeking someone to provide ideas on matters of color and contrast for the current design of the website.
Ideas top menu types and menu navigation.

https://www.filevarko.net/s/7kq4mwtzpe9bhxd/Esqueleto%20de%20Interface.pdf

Target Market(s)

We sell consulting services Information Systems for medium and small businesses.

```html
<!DOCTYPE html>
<html lang="es">
<head>
<meta charset="utf-8">
<title>NVS – Contacto</title>
<link rel="stylesheet" href="https://fonts.googleapis.com/css2?family=Open+Sans:ital,wght@0,400;0,600;0,700;1,400&display=swap">
<style>
  :root {
    --page-bg: #f2f2f2;
    --cream: #efe3b1;
    --rust: #c4612f;
    --rust-line: #d4825a;
    --white: #ffffff;
    --ink: #222222;
    --muted: #a8a8a8;
    --rule: #cfcfcf;
    --map-base: #e9e6df;
  }
  * { box-sizing: border-box; margin: 0; padding: 0; }
  html, body {
    width: 1200px; height: 650px; overflow: hidden;
    background: var(--page-bg);
    font-family: "Open Sans", Arial, sans-serif;
    color: var(--ink);
  }
  .site { position: relative; width: 1200px; height: 650px; }
  .wrap { position: absolute; left: 86px; width: 1028px; }

  /* Header */
  .masthead { top: 0; height: 68px; background: var(--cream); }
  .brand {
    position: absolute; left: 14px; top: 18px;
    display: flex; align-items: center; gap: 8px;
    font-size: 28px; font-weight: 600; color: var(--rust); letter-spacing: 1px;
  }
  .brand-mark { width: 28px; height: 28px; background: var(--rust); }
  .top-links { position: absolute; left: 350px; top: 22px; display: flex; gap: 9px; }
  .top-links a {
    display: block; height: 25px; line-height: 25px; padding: 0 17px;
    background: var(--white); color: var(--rust); font-size: 12px; text-decoration: none;
  }
  .top-links a:nth-child(2) { padding: 0 22px; }
  .social { position: absolute; right: 12px; top: 21px; display: flex; gap: 3px; }
  .social span { width: 25px; height: 26px; background: var(--white); display: block; }

  .main-nav { top: 68px; height: 37px; background: var(--rust); display: flex; }
  .main-nav a {
    display: block; height: 37px; line-height: 37px; padding: 0 25px;
    color: var(--white); font-size: 12px; text-decoration: none;
    border-right: 1px solid var(--rust-line);
  }
  .main-nav a:first-child { padding: 0 13px; font-size: 12.5px; }
  .main-nav .caret { font-size: 9px; margin-left: 4px; }

  /* Section headings */
  .section-title {
    position: absolute; display: flex; align-items: center; gap: 24px;
    font-size: 12px; color: var(--rust);
  }
  .section-title::after {
    content: ""; flex: 1; height: 6px;
    background: repeating-linear-gradient(to bottom, var(--rule) 0 1px, transparent 1px 2px);
  }

  /* Form */
  .field {
    position: absolute; background: var(--white); border: none;
    font-family: inherit; font-size: 11px; font-style: italic; color: var(--muted);
    padding: 0 12px; line-height: 26px; height: 26px;
  }
  .select {
    position: absolute; left: 544px; top: 183px; width: 214px; height: 26px;
    background: var(--white); color: var(--rust); font-size: 11.5px;
    line-height: 26px; padding-left: 12px;
  }
  .select .arrow {
    position: absolute; right: 0; top: 0; width: 25px; height: 26px; background: var(--cream);
  }
  .message { left: 86px; top: 226px; width: 672px; height: 155px; line-height: 26px; }
  .captcha-label {
    position: absolute; left: 86px; top: 398px; width: 60px; height: 26px;
    background: var(--cream); font-size: 11.5px; line-height: 26px; text-align: center;
  }
  .captcha-input {
    position: absolute; left: 146px; top: 398px; width: 154px; height: 26px;
    background: var(--white); color: var(--rust); font-size: 12px; line-height: 26px; padding-left: 12px;
  }
  .required { position: absolute; left: 313px; top: 403px; font-size: 11.5px; color: var(--rust); }
  .send {
    position: absolute; left: 86px; top: 441px; width: 84px; height: 25px;
    background: var(--rust); color: var(--white); font-size: 11px; font-weight: 700;
    letter-spacing: .5px; text-align: center; line-height: 25px;
  }

  /* Map & info */
  .map {
    position: absolute; left: 784px; top: 176px; width: 330px; height: 154px;
    background: linear-gradient(135deg, var(--map-base), #e2ded4 60%, #ece9e2);
  }
  .info { position: absolute; left: 784px; font-size: 11.5px; }
  .info b { font-weight: 700; }

  /* Footer */
  .footer-rule {
    position: absolute; left: 86px; top: 541px; width: 1028px; height: 6px;
    background: repeating-linear-gradient(to bottom, var(--rule) 0 1px, transparent 1px 2px);
  }
  .footer {
    top: 582px; height: 33px; background: var(--rust);
    color: var(--white); font-size: 10.5px; line-height: 33px; padding-left: 13px;
  }
  .to-top {
    position: absolute; right: 13px; top: 0; width: 33px; height: 33px; background: var(--cream);
  }
  .to-top svg { position: absolute; left: 10px; top: 12px; }
</style>
</head>
<body>
<div class="site">
  <header class="wrap masthead">
    <div class="brand"><span class="brand-mark"></span>NVS</div>
    <nav class="top-links">
      <a href="#">Inicio</a>
      <a href="#">Acerca de Nosotros</a>
      <a href="#">Contactenos</a>
    </nav>
    <div class="social" aria-label="Redes sociales">
      <span></span><span></span><span></span><span></span><span></span>
    </div>
  </header>

  <nav class="wrap main-nav">
    <a href="#">Aquitectuca Empresaria</a>
    <a href="#">Gestion de Proyctos</a>
    <a href="#">Servicios de Infraesctuctura de IT</a>
    <a href="#">Middleware</a>
    <a href="#">Aplicaciones<span class="caret">&#8964;</span></a>
    <a href="#">Base de Datos</a>
  </nav>

  <h2 class="section-title" style="left:86px; top:138px; width:672px; font-weight:400;">Fancy Contact Form</h2>
  <div class="field" style="left:86px; top:183px; width:214px;">Your name here...</div>
  <div class="field" style="left:315px; top:183px; width:214px;">Your email here...</div>
  <div class="select">Select your question ?
    <span class="arrow">
      <svg width="25" height="26" viewBox="0 0 25 26"><path d="M8 11l4.5 4.5L17 11" fill="none" stroke="#c4612f" stroke-width="1.3"/></svg>
    </span>
  </div>
  <div class="field message">Write your message here...</div>
  <div class="captcha-label">2 + 2 =</div>
  <div class="captcha-input">4</div>
  <div class="required">Required *</div>
  <div class="send">SEND</div>

  <h2 class="section-title" style="left:784px; top:138px; width:330px; font-weight:400;">Map</h2>
  <div class="map" role="img" aria-label="Mapa de calles con la ubicación de la oficina"></div>

  <h2 class="section-title" style="left:784px; top:361px; width:330px; font-weight:400;">Info</h2>
  <p class="info" style="top:396px;"><b>Address:</b> Calle Olmo 742 Piso 2 B</p>
  <p class="info" style="top:423px;"><b>Phone:</b> 5210/3381 ; 5294/0712 ; 5210/4468 ; 5294/0735</p>
  <p class="info" style="top:467px;"><b>Address:</b> Distrito Ribera Norte</p>
  <p class="info" style="top:494px;"><b>Phone:</b> 5236/8814 ; 5236/8815 ; 5236/8816</p>

  <div class="footer-rule"></div>
  <footer class="wrap footer">All reserved by: NVS
    <span class="to-top"><svg width="13" height="8" viewBox="0 0 13 8"><path d="M1 7l5.5-5.5L12 7" fill="none" stroke="#c4612f" stroke-width="1.3"/></svg></span>
  </footer>
</div>
</body>
</html>
```